Internal Office Slogans / Motto / Vision Statements

Hi. We would like to put up some posters around the office with quotations such as -
-”Do what you do so well that they will want to see it again and bring their friends.”- Hollis Trevane
-Make your customers feel heard and understood. Make your customers feel respected and liked. Make your customers feel appreciated and helped. Understand that you can do none of these things unless you are sincere about them.
Gregory Pilcott
- It’s a very predictable and satisfying phenomenon: whenever we get better, our customers do too.
Ray Casso
-Catch people in the act of performing extraordinary customer service. Treat them like heroes. Tell their stories, far and wide.
Tod Brinkerley

The purpose of the posters is to reiterate our culture and vision within the organisation. They should be clean, crisp and eye catching, not gaudy or bright. Professional, bold and strong.

The company website and logo is at http://www.nexolux.com.au
Print size will be A1

Thanks for participating & looking forward to seeing your great work.
Updates

Hi All. . 

So to reiterate we are looking for one background design to be used for multiple quotes...  The list of quotes are as follows: 

Support and or Sales Office

 

Make your customers feel heard and understood.Make your customers feel respected and liked. Make your customers feelappreciated and helped. Understand that you can do none of these things unlessyou are sincere about them.

Gregory Pilcott

 

Nothing liberates our greatness like the desireto help, the desire to serve

Rosalind Penhallow

 

It’s a very predictable and satisfying phenomenon:whenever we get better, our customers do too.

Ray Casso

 

Success means we go to sleep at night knowingthat our talents and abilities were used in a way that served others.

Rosalind Penhallow.

 

The sole purpose of business is to create, serveand satisfy a customer, from beginning to end – and that’s everyone’s job.

Tod Brinkerley

 

We don’t celebrate closing a sale, we celebrateopening a relationship.

Gwendolyn Asque

I will never make you a promise – unless I giveyou a plan and procedure to make that promise possible.

Bo Tarrick

 

Customers feel we take them for granted; onlyshow interest when we want an order; lavish our time on prospects; communicatemainly by invoice; are fixated on big accounts; drop them like hot potatoesonce we have the order; don’t follow through on promises; and satisfy our ownbureaucracy rather than their needs. We can do better than that, much better.

Peter L Osmund.

 

 

General and public area

 

Catch people in the act of performingextraordinary customer service. Treat them like heroes. Tell their stories, farand wide.

Tod Brinkerley

 

 

We see our customers as invited guests to aparty, and we are the hosts. It’s our job every day to make every importantaspect of the customer experience a little bit better." Carl Ingvold - Founder andCEO of Veltrix

 

"If you do build a great experience,customers tell each other about that. Word of mouth is verypowerful."  Carl Ingvold

 

It's not a faithin technology. It's faith in people. Neil Corrby

 

“Being the richest man in the cemetery doesn’tmatter to me … Going to bed at night saying we’ve done something wonderful…that’s what matters to me.” Neil Corrby

 

The customer experience is the next competitivebattleground. Lance Merriwether, CIO, Quorra Computers

 

”Do what you do so well that they will want tosee it again and bring their friends.”- Hollis Trevane

In the world of internet customer service, it isimportant to remember your competitor is only a mouse click away. GlenTrasky (not sure who he is but like the quote).

The customer is why you go to work. If they goaway, you do, too. Martin Glossop (?)

 

MaybeSome for Sales or Build Team:

Quality is remembered long after the price is forgotten. Varenne Family Slogan

```html
<!DOCTYPE html>
<html lang="en">
<head>
<meta charset="utf-8">
<title>Catch People in the Act — Office Poster</title>
<link rel="stylesheet" href="https://fonts.googleapis.com/css2?family=Montserrat:wght@700;800&family=Questrial&display=swap">
<style>
  :root {
    --ink: #ffffff;
    --shadow: rgba(20, 12, 4, 0.75);
    --slate: #262c35;
    --smoke: #4a4a44;
    --amber: #c98a22;
    --ember: #c65a12;
    --umber: #3a220f;
    --gold: #e8c544;
    --rule: rgba(255, 255, 255, 0.95);
  }
  html, body {
    margin: 0;
    padding: 0;
    width: 848px;
    height: 1200px;
    overflow: hidden;
    background: var(--slate);
  }
  .poster {
    position: relative;
    width: 848px;
    height: 1200px;
    overflow: hidden;
  }
  .poster__backdrop {
    position: absolute;
    inset: 0;
    background:
      radial-gradient(ellipse 260px 320px at 560px 720px, rgba(232, 197, 68, 0.75), transparent 70%),
      radial-gradient(ellipse 220px 260px at 640px 300px, rgba(232, 160, 40, 0.7), transparent 70%),
      radial-gradient(ellipse 200px 300px at 820px 160px, rgba(198, 90, 18, 0.8), transparent 70%),
      radial-gradient(ellipse 240px 200px at 420px 1150px, rgba(232, 197, 68, 0.55), transparent 70%),
      radial-gradient(ellipse 260px 500px at 60px 600px, rgba(30, 36, 46, 0.9), transparent 75%),
      linear-gradient(90deg, var(--slate) 0%, var(--smoke) 35%, var(--amber) 70%, var(--ember) 88%, var(--umber) 100%);
  }
  .quote {
    position: absolute;
    inset: 0;
    margin: 0;
    color: var(--ink);
    text-transform: uppercase;
    text-align: center;
  }
  .line {
    position: absolute;
    left: 0;
    right: 0;
    line-height: 1;
    transform: translateY(-50%);
    white-space: nowrap;
    text-shadow: 3px 4px 5px var(--shadow);
  }
  .light {
    font-family: "Questrial", sans-serif;
    font-weight: 400;
    font-size: 64px;
    letter-spacing: 1px;
  }
  .strong {
    font-family: "Montserrat", sans-serif;
    font-weight: 700;
  }
  .line--catch { top: 86px; }
  .line--act { top: 186px; }
  .line--performing { top: 282px; }
  .line--extraordinary { top: 380px; font-size: 60px; letter-spacing: 1px; }
  .line--customer { top: 480px; font-size: 66px; letter-spacing: 1px; }
  .line--service { top: 580px; font-size: 84px; letter-spacing: 2px; font-weight: 800; }
  .line--treat { top: 676px; }
  .line--heroes { top: 772px; font-size: 86px; letter-spacing: 2px; font-weight: 800; }
  .line--stories { top: 872px; font-size: 58px; }
  .line--stories .strong { font-size: 56px; }
  .line--wide { top: 936px; font-size: 44px; letter-spacing: 1px; }
  .divider {
    position: absolute;
    left: 0;
    top: 1038px;
    width: 848px;
    height: 6px;
  }
  .attribution {
    position: absolute;
    left: 0;
    right: 0;
    top: 1113px;
    margin: 0;
    transform: translateY(-50%);
    line-height: 1;
    text-align: center;
    color: var(--ink);
    font-family: "Montserrat", sans-serif;
    font-weight: 700;
    font-size: 50px;
    letter-spacing: 1px;
    text-transform: uppercase;
    text-shadow: 3px 4px 5px var(--shadow);
  }
</style>
</head>
<body>
<main class="poster">
  <div class="poster__backdrop" role="img" aria-label="Soft blurred bokeh lights in slate, amber and orange tones"></div>

  <blockquote class="quote">
    <div class="line line--catch light">Catch people</div>
    <div class="line line--act light">In the <span class="strong">act</span> of</div>
    <div class="line line--performing light">Performing</div>
    <div class="line line--extraordinary strong">Extraordinary</div>
    <div class="line line--customer strong">Customer</div>
    <div class="line line--service strong">Service.</div>
    <div class="line line--treat light">Treat them like</div>
    <div class="line line--heroes strong">Heroes.</div>
    <div class="line line--stories light">Tell their <span class="strong">stories.</span></div>
    <div class="line line--wide strong">Far and wide.</div>
  </blockquote>

  <svg class="divider" viewBox="0 0 848 6" aria-hidden="true">
    <line x1="0" y1="3" x2="848" y2="3" stroke="var(--rule)" stroke-width="3" stroke-dasharray="7 4"/>
  </svg>

  <p class="attribution">-Tod Brinkerley</p>
</main>
</body>
</html>
```